Security Warning Sign

We have an existing sign that needs an update. I have attached a picture of the current square sign. We need to maintain the same wording. It needs to be professional and appropriate to attach to our customers fence. Also attached is a copy of our building sign which may lend some inspiration and hopefully the ai format will assist. The final sign will be 600mm x 600mmOur website is www.halvorngate.com.au

```html
<!DOCTYPE html>
<html lang="en">
<head>
<meta charset="utf-8">
<title>Security Warning Sign</title>
<link rel="stylesheet" href="https://fonts.googleapis.com/css2?family=Anton&family=Oswald:wght@700&family=Montserrat:wght@800&display=swap">
<style>
  :root {
    --sign-orange: #f28a1e;
    --panel-white: #ffffff;
    --ink-black: #0d0d0d;
    --page-bg: #e9e9e9;
  }
  html, body {
    margin: 0;
    padding: 0;
    width: 1200px;
    height: 900px;
    overflow: hidden;
    background: var(--page-bg);
  }
  .sign {
    position: absolute;
    left: 180px;
    top: 30px;
    width: 840px;
    height: 840px;
    overflow: hidden;
  }
  .sign-shapes {
    position: absolute;
    inset: 0;
  }
  .sign-title {
    position: absolute;
    left: 0;
    top: 8px;
    width: 840px;
    margin: 0;
    text-align: center;
    font-family: "Anton", "Impact", sans-serif;
    font-size: 228px;
    line-height: 1;
    letter-spacing: -2px;
    color: var(--panel-white);
  }
  .sign-message {
    position: absolute;
    left: 50px;
    top: 262px;
    width: 740px;
    margin: 0;
    text-align: center;
    font-family: "Oswald", "Arial Narrow", sans-serif;
    font-weight: 700;
    font-size: 70px;
    line-height: 82px;
    text-transform: uppercase;
    color: var(--ink-black);
  }
  .brand {
    position: absolute;
    left: 60px;
    top: 712px;
    display: flex;
    align-items: center;
    gap: 16px;
  }
  .brand-dot {
    width: 84px;
    height: 84px;
    border-radius: 50%;
    background: var(--sign-orange);
    flex: none;
  }
  .brand-name {
    font-family: "Montserrat", sans-serif;
    font-weight: 800;
    font-size: 26px;
    line-height: 31px;
    color: var(--panel-white);
    text-transform: uppercase;
  }
  .contact {
    position: absolute;
    left: 505px;
    top: 752px;
    width: 325px;
    color: var(--panel-white);
    font-family: "Montserrat", sans-serif;
    font-weight: 800;
    white-space: nowrap;
  }
  .contact-phone {
    display: flex;
    align-items: center;
    gap: 8px;
    font-size: 34px;
    line-height: 1;
  }
  .phone-icon {
    flex: none;
  }
  .contact-web {
    margin-top: 12px;
    padding-left: 6px;
    font-size: 13.5px;
    letter-spacing: 0.2px;
    text-transform: uppercase;
  }
</style>
</head>
<body>
  <div class="sign">
    <svg class="sign-shapes" width="840" height="840" viewBox="0 0 840 840">
      <rect class="sign-field" x="0" y="0" width="840" height="840" fill="var(--sign-orange)"/>
      <rect class="message-panel" x="50" y="240" width="740" height="490" fill="var(--panel-white)"/>
      <polygon class="panel-slash" points="470,700 530,700 440,840 380,840" fill="var(--panel-white)"/>
      <polygon class="brand-band" points="30,690 495,690 405,840 30,840" fill="var(--ink-black)"/>
      <polygon class="contact-band" points="540,730 840,730 840,840 470,840" fill="var(--sign-orange)"/>
    </svg>

    <h1 class="sign-title">WARNING</h1>

    <p class="sign-message">Electronic<br>Surveillance and<br>Recording Devices<br>Installed in this<br>Area Halvorngate</p>

    <div class="brand">
      <span class="brand-dot"></span>
      <div class="brand-name">Halvorngate<br>Security<br>Services</div>
    </div>

    <div class="contact">
      <div class="contact-phone">
        <svg class="phone-icon" width="30" height="30" viewBox="0 0 24 24" aria-hidden="true">
          <path fill="#ffffff" d="M6.6 10.8c1.4 2.8 3.8 5.1 6.6 6.6l2.2-2.2c.3-.3.7-.4 1-.2 1.1.4 2.3.6 3.6.6.6 0 1 .4 1 1V20c0 .6-.4 1-1 1C10.6 21 3 13.4 3 4c0-.6.4-1 1-1h3.5c.6 0 1 .4 1 1 0 1.3.2 2.5.6 3.6.1.3 0 .7-.2 1L6.6 10.8z"/>
        </svg>
        <span>1300 555 418</span>
      </div>
      <div class="contact-web">www.halvorngate.com.au</div>
    </div>
  </div>
</body>
</html>
```